Seafood Restaurant Outdoor Menu Board

Corvell's Seafood, a legendary local seafood restaurant in Ventura, CA USA, most widely known for its fish and chips and clam chowder, needs refreshed outdoor menu boards!

You can see the existing menu board at https://www.pictoshare.example/p/K8mR2Wxq51T/

and get inspiration from our website, https://corvellsseafood.example

Please use your design for 2 sets of menu items, to be displayed side by side as in the photo:
Menu Board #1: "Customer Favorites"
- Grilled Halibut
- Grilled Salmon Filet
- Grilled Shrimp Skewers
- Corvell's Fish & Chips
- 14pc Shrimp & Chips
- Harbor Trio
- Onion Rings
- Clam Chowder Lantern
- Large Clam Chowder
- Small Clam Chowder
Menu Board #2: "Grilled Dinners"
GR HALIBUT $21.80
BAKED HALIBUT $26.95
GR SNAPPER $21.95
GR AHI $25.85
GR SALMON FILLET $20.90
GR YELLOWTAIL $12.65
GR BLACK SEA BASS $20.99
GR SHRIMP SKEWERS $23.10
GR WHITE SEA BASS $21.60
GR SWORDFISH $27.75
GR MAHI $7.95
GR COD $10.40

SERVED WITH RICE PILAF & BREAD & YOUR CHOICE OF PASTA SALAD, COLE SLAW, OR GREEN SALAD

Our landlord has provided the following guidelines for the new menu board:
- Public Facing Exterior Menu boards need overall simplification and reduction of the information offered while still highlighting major sellers and up sellers.
- Need to be designed as elegant wall signs rather than a list of menu items. (see examples)
- Less is More.
- Easy to read and understand, equally spaced information, good use of negative space.
- Draw customers eyes to the most desirable products.
- Layout: The layout should be professionally done, with sufficient negative space around menu items.
- Fonts: 3 Fonts maximum, encouraging sans serif font styles for easy readability.
- Established 1982: Arial Rounded MT Bold
- Menu Boards: Myriad Pro - Bold Condensed
- Smaller Directional Signs: Arial
- Colors: Tied to organization branding, 3 colors maximum. Please use a light-colored background. Our brand colors are:
- Primary: #233F94
- Secondary: #0F65A7
- Tertiary: 32A0CA
- Contrast: #F7F4DB
Attention: #ED4224
Icons: Use of simplified icons are allowed and encouraged to highlight and organize menu sections

```html
<!DOCTYPE html>
<html lang="en">
<head>
<meta charset="utf-8">
<title>Grilled Dinners – Corvell's Seafood</title>
<link rel="stylesheet" href="https://fonts.googleapis.com/css2?family=Open+Sans:wdth,wght@75..100,700;75..100,800&display=swap">
<style>
  :root {
    --ink: #253f92;
    --wash-light: #f2f8fc;
    --wash-mid: #cfe6f4;
    --wash-deep: #9ccbe6;
    --sketch: rgba(37, 63, 146, 0.16);
  }
  html, body {
    margin: 0;
    padding: 0;
    overflow: hidden;
  }
  body {
    width: 849px;
    height: 1200px;
  }
  .menu-board {
    position: relative;
    width: 849px;
    height: 1200px;
    overflow: hidden;
    background:
      radial-gradient(ellipse at 30% 20%, var(--wash-light) 0%, transparent 55%),
      radial-gradient(ellipse at 80% 75%, var(--wash-light) 0%, transparent 50%),
      radial-gradient(ellipse at 15% 85%, var(--wash-deep) 0%, transparent 45%),
      radial-gradient(ellipse at 85% 10%, var(--wash-deep) 0%, transparent 40%),
      linear-gradient(160deg, var(--wash-mid) 0%, var(--wash-light) 45%, var(--wash-mid) 100%);
    font-family: "Open Sans", Arial, sans-serif;
    color: var(--ink);
  }
  .sketch {
    position: absolute;
    background: var(--sketch);
    border-radius: 50%;
  }
  .sketch--crab { left: 195px; top: -30px; width: 270px; height: 135px; }
  .sketch--lemon-top { left: 600px; top: -20px; width: 135px; height: 125px; }
  .sketch--oyster-top { left: 705px; top: -30px; width: 150px; height: 90px; }
  .sketch--herb-top { left: -20px; top: -10px; width: 125px; height: 190px; border-radius: 40%; }
  .sketch--fish { left: 630px; top: 135px; width: 240px; height: 215px; border-radius: 48% 40% 45% 55%; }
  .sketch--lemon-left { left: -35px; top: 428px; width: 133px; height: 128px; }
  .sketch--oyster-right { left: 728px; top: 458px; width: 140px; height: 172px; border-radius: 45%; }
  .sketch--herb-right { left: 780px; top: 765px; width: 80px; height: 75px; border-radius: 40%; }
  .sketch--lemon-right { left: 788px; top: 848px; width: 125px; height: 128px; }
  .sketch--shrimp { left: -20px; top: 983px; width: 155px; height: 230px; border-radius: 45%; }
  .sketch--mussel { left: 780px; top: 1005px; width: 90px; height: 135px; border-radius: 50% 50% 45% 45%; }
  .sketch--oyster-bottom { left: 660px; top: 1140px; width: 150px; height: 100px; }

  .board-title {
    position: absolute;
    left: 88px;
    top: 122px;
    margin: 0;
    font-weight: 800;
    font-stretch: 82%;
    font-variation-settings: "wdth" 82;
    font-size: 162px;
    line-height: 131px;
    letter-spacing: -2px;
    text-transform: uppercase;
  }
  .dinner-list {
    position: absolute;
    left: 128px;
    top: 421px;
    width: 560px;
    margin: 0;
    padding: 0;
    list-style: none;
  }
  .dinner-item {
    display: flex;
    justify-content: space-between;
    height: 51.3px;
    line-height: 40px;
    font-weight: 800;
    font-size: 27px;
    text-transform: uppercase;
  }
  .dinner-item__price {
    width: 110px;
  }
  .sides-note {
    position: absolute;
    left: 128px;
    top: 1062px;
    margin: 0;
    font-weight: 800;
    font-size: 22.5px;
    line-height: 33px;
    text-transform: uppercase;
  }
</style>
</head>
<body>
<main class="menu-board">
  <div class="sketch sketch--crab" role="img" aria-label="Line sketch of a crab"></div>
  <div class="sketch sketch--lemon-top" role="img" aria-label="Line sketch of a lemon slice"></div>
  <div class="sketch sketch--oyster-top" role="img" aria-label="Line sketch of an oyster"></div>
  <div class="sketch sketch--herb-top" role="img" aria-label="Line sketch of a rosemary sprig"></div>
  <div class="sketch sketch--fish" role="img" aria-label="Line sketch of a whole fish"></div>
  <div class="sketch sketch--lemon-left" role="img" aria-label="Line sketch of a lemon slice"></div>
  <div class="sketch sketch--oyster-right" role="img" aria-label="Line sketch of an oyster on the half shell"></div>
  <div class="sketch sketch--herb-right" role="img" aria-label="Line sketch of a rosemary sprig"></div>
  <div class="sketch sketch--lemon-right" role="img" aria-label="Line sketch of a lemon slice"></div>
  <div class="sketch sketch--shrimp" role="img" aria-label="Line sketch of a shrimp"></div>
  <div class="sketch sketch--mussel" role="img" aria-label="Line sketch of a mussel"></div>
  <div class="sketch sketch--oyster-bottom" role="img" aria-label="Line sketch of an oyster"></div>

  <h1 class="board-title">Grilled<br>Dinners</h1>

  <ul class="dinner-list">
    <li class="dinner-item"><span>GR Halibut</span><span class="dinner-item__price">$21.80</span></li>
    <li class="dinner-item"><span>Baked Halibut</span><span class="dinner-item__price">$26.95</span></li>
    <li class="dinner-item"><span>GR Snapper</span><span class="dinner-item__price">$21.95</span></li>
    <li class="dinner-item"><span>GR Ahi</span><span class="dinner-item__price">$25.85</span></li>
    <li class="dinner-item"><span>GR Salmon Fillet</span><span class="dinner-item__price">$20.90</span></li>
    <li class="dinner-item"><span>GR Yellowtail</span><span class="dinner-item__price">$12.65</span></li>
    <li class="dinner-item"><span>GR Black Sea Bass</span><span class="dinner-item__price">$20.99</span></li>
    <li class="dinner-item"><span>GR Shrimp Skewers</span><span class="dinner-item__price">$23.10</span></li>
    <li class="dinner-item"><span>GR White Sea Bass</span><span class="dinner-item__price">$21.60</span></li>
    <li class="dinner-item"><span>GR Swordfish</span><span class="dinner-item__price">$27.75</span></li>
    <li class="dinner-item"><span>GR Mahi</span><span class="dinner-item__price">$7.95</span></li>
    <li class="dinner-item"><span>GR Cod</span><span class="dinner-item__price">$10.40</span></li>
  </ul>

  <p class="sides-note">Served with rice pilaf &amp; bread &amp; your choice of<br>pasta salad, cole slaw, or green salad</p>
</main>
</body>
</html>
```